Property Management Card

We are owners of a property management and real estate company. We manage many residential buildings in our area and would like to send cards to neighboring propertiies. I have attached a card that was designed for us that we do not like but has pertinent information and branding, font style, etc. We want something that will grab people's attention as they sift through their junk mail.

Here is information we would like included:

We manage the property at________(we will fill in the blank)
We can manage yours, too!

We offer
24 hour emergency line
online rent payment for tenants
the best trades people in the South Bay
5 full time employees who speak English and Spanish
Business for over 36 years

Call BrentOlley for a free quote at 310-847-2913

Target Market(s)

Industry/Entity Type

Real Estate

Requirements
Must have
• We manage the property at________(we will fill in the blank)
• We can manage yours, too!
• We offer
• 24 hour emergency line
• online rent payment for tenants
• the best trades people in the South Bay
• 5 full time employees who speak English and Spanish
• Business for over 36 years
• Call BrentOlley for a free quote at 310-847-2913
• Email address brent@harborlinemgmt.example
• website westridgecoastalrentals.example
• Broker BRE 04718392
• office address is
• 48 Corvina Ridge Court, Suite 1
• Palos Verdes Estates, CA 90388
• two sided
• space for a mailing address and postage
• our branding/logo
• font to coordinate with branding
• postcard to be 279mm x 152 mm (full bleed size is 282 mm x 155mm, 3335x1835 pixels)
• vertical or horizontal orientation up to designers creativity. Again, what ever will draw attention
• (our branding colors are a dark gray/charcoal, white and dark sand. see postcard and logo for example of colors)
Nice to have
• images to draw attention to owners who would like a property manager
• we would like to have our photo. if this compromises design then we are happy to delete it. the photo can be on either side

```html
<!DOCTYPE html>
<html lang="en">
<head>
<meta charset="utf-8">
<title>Westridge Partners – Property Management Postcard</title>
<link rel="stylesheet" href="https://fonts.googleapis.com/css2?family=Roboto:wght@400;500;700&family=Open+Sans:wght@400;600&display=swap">
<style>
:root{
  --stage:#625a4c;
  --charcoal:#393432;
  --sand:#8f8a78;
  --sand-light:#a9a494;
  --paper:#f7f7f5;
  --band:#efefef;
  --ink:#3a3533;
  --white:#ffffff;
}
*{margin:0;padding:0;box-sizing:border-box}
html,body{width:1200px;height:1031px;overflow:hidden}
body{background:var(--stage);font-family:"Roboto",Arial,sans-serif;color:var(--white);position:relative}
.card{position:absolute;left:256px;width:688px;height:374px;overflow:hidden}
.front{top:124px;background:var(--charcoal)}
.back{top:531px;background:var(--paper)}
.abs{position:absolute}

/* front */
.topband{left:0;top:0;width:688px;height:44px;background:var(--band);z-index:3}
.topband h1{position:absolute;left:23px;top:14px;font-size:14px;font-weight:700;color:var(--ink);letter-spacing:-.1px}
.subhead{left:23px;top:51px;font-size:14px;font-weight:700}
.offer-box{left:23px;top:85px;width:211px;height:27px;border:1.5px solid var(--sand-light);font-size:11px;font-weight:700;display:flex;align-items:center;justify-content:center}
.offers{list-style:none;font-size:11px;line-height:17.3px}
.offers li{display:flex;align-items:center;white-space:nowrap}
.offers svg{width:10px;height:10px;margin-right:17px;flex:none}
.front .offers{left:23px;top:120px}
.call-box{left:23px;top:224px;width:367px;height:51px;border:1.5px solid var(--sand-light);display:flex;align-items:center;padding-left:15px;white-space:nowrap}
.call-tag{left:45px;top:216px;width:53px;height:15px;background:var(--sand);font-size:10px;font-weight:700;display:flex;align-items:center;justify-content:center}
.call-name{font-size:19px;font-weight:700}
.call-mid{font-size:11px;margin:0 8px 0 6px}
.call-phone{font-size:20px;font-weight:700;letter-spacing:.3px}
.weblinks{left:23px;top:290px;font-size:11px;display:flex;gap:14px;white-space:nowrap}
.weblinks .sep{color:var(--sand-light)}
.sandband{left:0;top:320px;width:688px;height:54px;background:var(--sand);z-index:0}
.contact{font-size:10px;line-height:13.5px;color:#f3f1ea;display:flex;align-items:center;gap:10px;white-space:nowrap;z-index:1}
.contact svg{width:19px;height:19px;flex:none}
.photo-ring{left:418px;top:68px;width:464px;height:464px;border-radius:50%;background:var(--sand);z-index:1}
.photo{left:426px;top:76px;width:448px;height:448px;border-radius:50%;background:radial-gradient(circle at 30% 55%,#6e5a4c 0%,#3f3732 45%,#8c8a86 100%);z-index:1}

.brand{font-family:"Open Sans",Arial,sans-serif;color:var(--white)}
.brand .name{font-size:24px;font-weight:400;line-height:25px;letter-spacing:.4px}
.brand .tag{font-size:7px;letter-spacing:1.6px;margin-top:8px;font-weight:600}
.logo-box{left:284px;top:60px;width:198px;height:94px;border:1.5px solid var(--sand-light);background:var(--charcoal);padding:14px 0 0 20px;z-index:2}

/* back */
.back-panel{left:0;top:0;width:688px;height:374px}
.back .brand{left:33px;top:34px}
.back .brand .name{font-size:26px;line-height:27px}
.back-head{left:34px;top:140px;font-size:11px;font-weight:700}
.back .offers{left:34px;top:167px}
.back .offers li.cont{padding-left:27px}
.back-contacts{left:34px;top:304px;font-size:9.5px;line-height:12.5px;white-space:nowrap}
.back-contacts div{display:flex;align-items:center}
.back-contacts svg{width:9px;height:9px;margin-right:8px;flex:none}
.back-contacts .indent{padding-left:17px}
.stamp{left:589px;top:44px;width:52px;height:51px;border:1px solid var(--ink)}
.addr-line{left:414px;width:227px;height:1px;background:var(--ink)}
</style>
</head>
<body>

<section class="card front" aria-label="Postcard front">
  <div class="abs sandband"></div>
  <div class="abs photo-ring"></div>
  <div class="abs photo" role="img" aria-label="Portrait photo of the two agency owners"></div>

  <div class="abs topband"><h1>WE MANAGE THE PROPERTY AT</h1></div>
  <h2 class="abs subhead">WE CAN MANAGE YOURS</h2>
  <div class="abs offer-box">HERE IS WHAT WE HAVE TO OFFER</div>

  <ul class="abs offers">
    <li><svg viewBox="0 0 10 10"><circle cx="5" cy="5" r="4" fill="none" stroke="#a9a494" stroke-width="1"/><path d="M3 5l1.6 1.6L9 2" fill="none" stroke="#a9a494" stroke-width="1"/></svg>24 hour emergency line</li>
    <li><svg viewBox="0 0 10 10"><circle cx="5" cy="5" r="4" fill="none" stroke="#a9a494" stroke-width="1"/><path d="M3 5l1.6 1.6L9 2" fill="none" stroke="#a9a494" stroke-width="1"/></svg>Online rent payment for tenants</li>
    <li><svg viewBox="0 0 10 10"><circle cx="5" cy="5" r="4" fill="none" stroke="#a9a494" stroke-width="1"/><path d="M3 5l1.6 1.6L9 2" fill="none" stroke="#a9a494" stroke-width="1"/></svg>The best trades people in the South Bay</li>
    <li><svg viewBox="0 0 10 10"><circle cx="5" cy="5" r="4" fill="none" stroke="#a9a494" stroke-width="1"/><path d="M3 5l1.6 1.6L9 2" fill="none" stroke="#a9a494" stroke-width="1"/></svg>5 full time employees who speak English and Spanish</li>
    <li><svg viewBox="0 0 10 10"><circle cx="5" cy="5" r="4" fill="none" stroke="#a9a494" stroke-width="1"/><path d="M3 5l1.6 1.6L9 2" fill="none" stroke="#a9a494" stroke-width="1"/></svg>Business for over 36 years</li>
  </ul>

  <div class="abs call-box">
    <span class="call-name">BrentOlley</span>
    <span class="call-mid">for a free quote at</span>
    <span class="call-phone">310-847-2913</span>
  </div>
  <div class="abs call-tag">CALL</div>

  <div class="abs weblinks">
    <span>www.westridgecoastalrentals.example</span><span class="sep">|</span><span>Broker BRE 04718392</span>
  </div>

  <div class="abs logo-box brand">
    <div class="name">WESTRIDGE<br>PARTNERS</div>
    <div class="tag">A BOUTIQUE REAL ESTATE AGENCY</div>
  </div>

  <div class="abs contact" style="left:23px;top:334px">
    <svg viewBox="0 0 20 20"><circle cx="10" cy="10" r="9" fill="none" stroke="#3a3533" stroke-width="1.2"/><rect x="5.5" y="7" width="9" height="6" fill="none" stroke="#3a3533" stroke-width="1.1"/><path d="M5.5 7l4.5 3.5L14.5 7" fill="none" stroke="#3a3533" stroke-width="1.1"/></svg>
    <div>brent@harborlinemgmt.example<br>www.harborlinemgmt.example</div>
  </div>
  <div class="abs contact" style="left:222px;top:335px">
    <svg viewBox="0 0 20 20"><circle cx="10" cy="10" r="9" fill="none" stroke="#3a3533" stroke-width="1.2"/><path d="M10 15s-3.5-3.6-3.5-6a3.5 3.5 0 017 0c0 2.4-3.5 6-3.5 6z" fill="#3a3533"/><circle cx="10" cy="9" r="1.2" fill="#8f8a78"/></svg>
    <div>48 Corvina Ridge Court, Suite 1<br>Palos Verdes Estates, CA 90388</div>
  </div>
</section>

<section class="card back" aria-label="Postcard back">
  <svg class="abs back-panel" viewBox="0 0 688 374" aria-hidden="true">
    <polygon points="0,0 412,0 288,374 0,374" fill="#393432"/>
    <polygon points="0,134 367,134 358,161 0,161" fill="#8f8a78"/>
    <polygon points="0,292 315,292 314,294 0,294" fill="#8f8a78"/>
  </svg>

  <div class="abs brand">
    <div class="name">WESTRIDGE<br>PARTNERS</div>
    <div class="tag">A BOUTIQUE REAL ESTATE AGENCY</div>
  </div>

  <div class="abs back-head">HERE IS WHAT WE HAVE TO OFFER</div>
  <ul class="abs offers">
    <li><svg viewBox="0 0 10 10"><circle cx="5" cy="5" r="4" fill="none" stroke="#a9a494" stroke-width="1"/><path d="M3 5l1.6 1.6L9 2" fill="none" stroke="#a9a494" stroke-width="1"/></svg>24 hour emergency line</li>
    <li><svg viewBox="0 0 10 10"><circle cx="5" cy="5" r="4" fill="none" stroke="#a9a494" stroke-width="1"/><path d="M3 5l1.6 1.6L9 2" fill="none" stroke="#a9a494" stroke-width="1"/></svg>Online rent payment for tenants</li>
    <li><svg viewBox="0 0 10 10"><circle cx="5" cy="5" r="4" fill="none" stroke="#a9a494" stroke-width="1"/><path d="M3 5l1.6 1.6L9 2" fill="none" stroke="#a9a494" stroke-width="1"/></svg>The best trades people in the South Bay</li>
    <li><svg viewBox="0 0 10 10"><circle cx="5" cy="5" r="4" fill="none" stroke="#a9a494" stroke-width="1"/><path d="M3 5l1.6 1.6L9 2" fill="none" stroke="#a9a494" stroke-width="1"/></svg>5 full time employees who speak</li>
    <li class="cont">English and Spanish</li>
    <li><svg viewBox="0 0 10 10"><circle cx="5" cy="5" r="4" fill="none" stroke="#a9a494" stroke-width="1"/><path d="M3 5l1.6 1.6L9 2" fill="none" stroke="#a9a494" stroke-width="1"/></svg>Business for over 36 years</li>
  </ul>

  <div class="abs back-contacts">
    <div><svg viewBox="0 0 10 10"><rect x="1" y="2.5" width="8" height="5.5" fill="#a9a494"/><path d="M1 2.5l4 3 4-3" fill="none" stroke="#393432" stroke-width=".8"/></svg>brent@harborlinemgmt.example</div>
    <div><svg viewBox="0 0 10 10"><circle cx="5" cy="5" r="4" fill="none" stroke="#a9a494" stroke-width="1"/><path d="M1 5h8M5 1c-2 2.5-2 5.5 0 8M5 1c2 2.5 2 5.5 0 8" fill="none" stroke="#a9a494" stroke-width=".8"/></svg>westridgecoastalrentals.example</div>
    <div><svg viewBox="0 0 10 10"><path d="M5 9.5S2 6.5 2 4.3a3 3 0 016 0C8 6.5 5 9.5 5 9.5z" fill="#a9a494"/><circle cx="5" cy="4.2" r="1" fill="#393432"/></svg>48 Corvina Ridge Court, Suite 1</div>
    <div class="indent">Palos Verdes Estates, CA 90388</div>
  </div>

  <div class="abs stamp" aria-label="Postage area"></div>
  <div class="abs addr-line" style="top:158px"></div>
  <div class="abs addr-line" style="top:191px"></div>
  <div class="abs addr-line" style="top:223px"></div>
</section>

</body>
</html>
```